Eastlane Holdings Card

I would like a modern, eye catching card based off my logo design.
Info to include:
Tomas Velden (Card Name)
eastlaneholdings.com (Website)
555 283 6091 (Office/fax)
555 736 2840 (Business Cell)
tomas@eastlaneholdings.com (Work email)

Target Market(s)

Commercial real estate brokers, property owners.

Colors
ec1f27
757575

Requirements
Must have
• Name and info above. Not be lame!:)

```html
<!DOCTYPE html>
<html lang="en">
<head>
<meta charset="utf-8">
<title>Eastlane Holdings Card</title>
<link rel="stylesheet" href="https://fonts.googleapis.com/css2?family=Lato:wght@400;700;900&family=Montserrat:wght@500;700;800&display=swap">
<style>
  :root {
    --brand-red: #a51d23;
    --brand-grey: #757575;
    --card-black: #1f1b1b;
    --card-white: #ffffff;
    --ink: #333333;
    --backdrop: #e6ebeb;
  }
  html, body {
    margin: 0;
    width: 1200px;
    height: 900px;
    overflow: hidden;
    background: var(--backdrop);
  }
  .canvas {
    position: relative;
    width: 1200px;
    height: 900px;
  }
  .card {
    position: absolute;
    left: 250px;
    width: 700px;
    height: 400px;
    box-shadow: 0 6px 18px rgba(0,0,0,0.12);
    overflow: hidden;
  }
  .card-front { top: 30px; background: var(--card-black); }
  .card-back { top: 470px; background: var(--card-white); }

  /* Front */
  .brand {
    position: absolute;
    left: 70px;
    top: 130px;
    display: flex;
    align-items: center;
    gap: 18px;
  }
  .brand-mark {
    width: 52px;
    height: 52px;
    border: 4px solid var(--brand-grey);
    box-sizing: border-box;
  }
  .brand-text { display: flex; flex-direction: column; }
  .brand-name {
    font-family: "Montserrat", sans-serif;
    font-weight: 800;
    font-size: 44px;
    letter-spacing: 1px;
    color: var(--brand-red);
    text-transform: uppercase;
    line-height: 1;
    white-space: nowrap;
  }
  .brand-tagline {
    display: flex;
    align-items: center;
    gap: 14px;
    margin-top: 10px;
  }
  .brand-tagline .rule {
    flex: 1;
    height: 3px;
    background: var(--brand-grey);
  }
  .brand-tagline span {
    font-family: "Montserrat", sans-serif;
    font-weight: 700;
    font-size: 15px;
    letter-spacing: 5px;
    color: var(--brand-grey);
    text-transform: uppercase;
    white-space: nowrap;
  }
  .website {
    position: absolute;
    right: 60px;
    bottom: 90px;
    font-family: "Lato", sans-serif;
    font-size: 20px;
    letter-spacing: 0.5px;
    color: #ffffff;
    white-space: nowrap;
  }

  /* Back */
  .accent-bar {
    position: absolute;
    left: 0;
    top: 230px;
    width: 34px;
    height: 34px;
    background: var(--brand-red);
  }
  .person {
    position: absolute;
    left: 56px;
    top: 214px;
    font-family: "Lato", sans-serif;
  }
  .person-name {
    font-weight: 900;
    font-size: 30px;
    color: var(--ink);
    text-transform: uppercase;
    letter-spacing: 0.5px;
    line-height: 1.05;
  }
  .person-title {
    font-size: 18px;
    color: var(--ink);
    text-transform: uppercase;
    letter-spacing: 1px;
  }
  .contact-line {
    position: absolute;
    left: 0;
    top: 0;
    width: 700px;
    height: 400px;
  }
  .contact-text {
    position: absolute;
    top: 318px;
    font-family: "Lato", sans-serif;
    font-size: 18px;
    color: var(--ink);
    letter-spacing: 0.3px;
    white-space: nowrap;
  }
  .office { left: 60px; }
  .cell { left: 240px; }
  .email { left: 405px; }
</style>
</head>
<body>
<div class="canvas">
  <section class="card card-front">
    <div class="brand">
      <div class="brand-mark"></div>
      <div class="brand-text">
        <div class="brand-name">Eastlane Holdings</div>
        <div class="brand-tagline">
          <div class="rule"></div>
          <span>Construction &amp; Roofing</span>
          <div class="rule"></div>
        </div>
      </div>
    </div>
    <div class="website">www.EASTLANEHOLDINGS.com</div>
  </section>

  <section class="card card-back">
    <div class="accent-bar"></div>
    <div class="person">
      <div class="person-name">Tomas Velden</div>
      <div class="person-title">President</div>
    </div>
    <svg class="contact-line" viewBox="0 0 700 400" aria-hidden="true">
      <line x1="118" y1="300" x2="700" y2="300" stroke="#333" stroke-width="1.5"/>
      <!-- office phone -->
      <circle cx="74" cy="300" r="15" fill="#fff" stroke="#333" stroke-width="1.5"/>
      <path d="M67 293 q-2 8 7 15 q8 6 13 3 l-3 -4 q-3 2 -6 -1 q-5 -4 -5 -8 l-2 -3 z" fill="#a51d23"/>
      <!-- fax -->
      <circle cx="106" cy="300" r="15" fill="#fff" stroke="#333" stroke-width="1.5"/>
      <rect x="98" y="297" width="16" height="9" rx="1.5" fill="#a51d23"/>
      <rect x="101" y="291" width="10" height="6" fill="#a51d23"/>
      <!-- cell -->
      <circle cx="260" cy="300" r="15" fill="#fff" stroke="#333" stroke-width="1.5"/>
      <rect x="254" y="291" width="12" height="18" rx="2" fill="none" stroke="#a51d23" stroke-width="2"/>
      <!-- email -->
      <circle cx="425" cy="300" r="15" fill="#fff" stroke="#333" stroke-width="1.5"/>
      <rect x="416" y="293" width="18" height="13" fill="#a51d23"/>
      <path d="M416 293 l9 7 l9 -7" fill="none" stroke="#fff" stroke-width="1.5"/>
    </svg>
    <div class="contact-text office">555 283 6091</div>
    <div class="contact-text cell">555 736 2840</div>
    <div class="contact-text email">tomas@EastlaneHoldings.com</div>
  </section>
</div>
</body>
</html>
```